Verdana Glen Website

I need a design of homepage for a health and wellness center. We considers self to be young and fresh and want something along that design. We want a main picture/logo/design (or all three), and underneath that 4 pictures to depict what services we do. The four services are Orthopedic Rehab, Neurological Rehab, Speech Pathology and Float. I have attached our logo, and some pictures that might be helpful, but the pictures don't have to be included. Here is an example of what I would like it look. http://pixelquarry.com/web-design/contests/brimlotts-website-design-needed-more-work-come-submit-517306/entries/84162975

Health

```html
<!DOCTYPE html>
<html lang="en">
<head>
<meta charset="utf-8">
<title>Verdana Glen Center for Health + Wellness</title>
<link href="https://fonts.googleapis.com/css2?family=Open+Sans:ital,wght@0,400;0,600;1,400&display=swap" rel="stylesheet">
<style>
:root{
  --teal:#5bb3a9;
  --teal-dark:#3f9c90;
  --teal-text:#3d9a8d;
  --green:#8db81b;
  --green-dark:#7aa113;
  --ink:#555;
  --ink-soft:#666;
  --grey-band:#e4e4e4;
  --panel:#e9e9e9;
  --strip:#f2f2f2;
  --footer:#2f2f2f;
  --btn:#5a5a5a;
}
*{box-sizing:border-box;margin:0;padding:0}
html,body{width:1000px;height:1200px;overflow:hidden}
body{font-family:"Open Sans",Arial,sans-serif;color:var(--ink);background:#fff;position:relative}
.wrap{position:absolute;left:84px;width:833px}

.site-header{position:absolute;top:0;left:0;width:1000px;height:88px}
.brand{position:absolute;left:84px;top:24px;display:flex;align-items:center;gap:10px}
.brand-dot{width:34px;height:34px;border-radius:50%;background:var(--teal)}
.brand-name{font-size:30px;color:var(--teal);font-weight:400;line-height:1}
.brand-sub{font-size:11px;color:var(--teal);line-height:1.2;margin-left:4px}
.call{position:absolute;right:85px;top:22px;text-align:right;display:flex;align-items:center;gap:10px}
.call-label{font-size:16px;color:var(--teal-text);line-height:1.1}
.call-number{font-size:20px;color:var(--green);font-weight:600;line-height:1.1}

.main-nav{position:absolute;top:88px;left:0;width:1000px;height:38px;background:linear-gradient(var(--teal),var(--teal-dark))}
.main-nav ul{list-style:none;display:flex;position:absolute;left:84px;top:0;height:38px}
.main-nav li{color:#fff;font-size:13px;line-height:38px;padding:0 22px;border-right:1px solid rgba(255,255,255,.25)}
.main-nav li.active{background:var(--green);padding:0 22px}
.search{position:absolute;left:732px;top:6px;width:185px;height:26px;background:#fff;border-radius:2px;font-size:11px;color:#999;line-height:26px;padding-left:9px}
.search svg{position:absolute;right:5px;top:5px}

.hero-band{position:absolute;top:126px;left:0;width:1000px;height:371px;background:var(--grey-band)}
.hero{position:absolute;left:83px;top:139px;width:834px;height:341px;background:#fff;overflow:hidden}
.hero-photo{position:absolute;left:0;top:0;width:600px;height:341px;background:linear-gradient(90deg,#b9b383 0%,#d9cfa1 40%,#ede9df 75%,#fff 100%)}
.hero-copy{position:absolute;right:28px;top:76px;text-align:right}
.hero-copy h2{font-size:25px;font-weight:400;color:#555;line-height:1.2}
.btn-more{display:inline-block;margin-top:14px;background:var(--btn);color:#fff;font-size:13px;padding:9px 13px;border-radius:3px}
.hero-arrows{position:absolute;right:20px;top:299px;display:flex;gap:5px}

.services{position:absolute;top:524px;left:84px;width:833px;display:flex;gap:21px}
.service{width:192px;text-align:center}
.service h3{font-size:16px;font-weight:400;color:var(--teal-text);margin-bottom:6px;line-height:20px;white-space:nowrap}
.service .pic{height:122px}
.service .bar{height:6px;background:var(--teal);margin-top:2px}

.welcome{position:absolute;left:85px;top:712px;width:620px}
.welcome h1{font-size:27px;font-weight:400;color:var(--green);line-height:1.1}
.welcome h2{font-size:20px;font-weight:400;color:var(--teal-text);line-height:1.2}
.welcome p{font-size:11.5px;line-height:19px;color:var(--ink-soft);margin-top:12px}
.divider{height:1px;background:#ddd;margin-top:20px}
.quote{text-align:center;margin-top:20px;font-style:italic;font-size:15px;line-height:23px;color:#444}
.quote cite{display:block;font-style:normal;font-size:13.5px;color:#2a8fc2;margin-top:5px}

.contact-box{position:absolute;left:724px;top:718px;width:193px;height:282px;background:var(--panel)}
.contact-box h3{background:linear-gradient(var(--green),var(--green-dark));color:#fff;font-weight:400;font-size:16px;padding:5px 10px;height:31px}
.field{margin:10px 9px 0;background:#fff;border:1px solid #ddd;height:29px;font-size:11px;color:#888;padding:7px 11px}
.field + .field{margin-top:7px}
.field.message{height:91px}
.btn-submit{position:absolute;right:9px;bottom:12px;background:var(--btn);color:#fff;font-size:12px;padding:6px 9px;border-radius:3px}

.info-strip{position:absolute;top:1040px;left:0;width:1000px;height:80px;background:var(--strip)}
.info{position:absolute;top:0;height:80px;display:flex;align-items:center;gap:10px;font-size:11.5px;line-height:19px;color:#666}

.site-footer{position:absolute;top:1120px;left:0;width:1000px;height:80px;background:var(--footer);color:#bbb;font-size:11px}
.foot-links{position:absolute;left:84px;top:18px}
.foot-links span{margin:0 8px}
.copyright{position:absolute;left:84px;top:49px}
.social{position:absolute;right:83px;top:34px;display:flex;gap:8px}
.social i{width:21px;height:21px;border-radius:50%;background:var(--green);display:block}
</style>
</head>
<body>

<header class="site-header">
  <div class="brand">
    <span class="brand-dot"></span>
    <span class="brand-name">Verdana Glen</span>
  </div>
  <div class="call">
    <div>
      <div class="call-label">Call us</div>
      <div class="call-number">555 301 4827</div>
    </div>
    <svg width="26" height="22" viewBox="0 0 26 22"><path d="M3 4c2-3 4-3 5-1l2 3c1 2-1 3-2 4 1 3 3 5 6 6 1-1 2-3 4-2l3 2c2 1 2 3-1 5-6 3-20-10-17-17z" fill="var(--teal)"/></svg>
  </div>
</header>

<nav class="main-nav">
  <ul>
    <li class="active">HOME</li>
    <li>ABOUT US</li>
    <li>SERVICES</li>
    <li>TESTIMONIALS</li>
    <li>CONTACT US</li>
  </ul>
  <div class="search">Search
    <svg width="16" height="16" viewBox="0 0 16 16"><circle cx="6.5" cy="6.5" r="5" fill="none" stroke="#999" stroke-width="2"/><path d="M10 10l5 5" stroke="#999" stroke-width="2.4"/></svg>
  </div>
</nav>

<div class="hero-band"></div>
<section class="hero">
  <div class="hero-photo" role="img" aria-label="Smiling older couple outdoors in a sunny field"></div>
  <div class="hero-copy">
    <h2>Donec ornare eleifend enim<br>varius ullamcorper</h2>
    <span class="btn-more">Know more</span>
  </div>
  <div class="hero-arrows">
    <svg width="22" height="22" viewBox="0 0 22 22"><circle cx="11" cy="11" r="11" fill="#666"/><path d="M13 6l-5 5 5 5" stroke="#fff" stroke-width="2.2" fill="none"/></svg>
    <svg width="22" height="22" viewBox="0 0 22 22"><circle cx="11" cy="11" r="11" fill="#666"/><path d="M9 6l5 5-5 5" stroke="#fff" stroke-width="2.2" fill="none"/></svg>
  </div>
</section>

<section class="services">
  <div class="service"><h3>ORTHOPEDIC REHAB</h3><div class="pic" role="img" aria-label="Therapist treating a patient's knee" style="background:linear-gradient(#e8ecf2,#d9b49a)"></div><div class="bar"></div></div>
  <div class="service"><h3>NEUROLOGICAL REHAB</h3><div class="pic" role="img" aria-label="Treatment pod in a dim room" style="background:linear-gradient(#8a8a88,#3f4a5e)"></div><div class="bar"></div></div>
  <div class="service"><h3>SPEECH PATHOLOGY</h3><div class="pic" role="img" aria-label="Therapist working with a young patient" style="background:linear-gradient(#d8cdb6,#8a8f8c)"></div><div class="bar"></div></div>
  <div class="service"><h3>FLOAT</h3><div class="pic" role="img" aria-label="Bright gym with exercise machines" style="background:linear-gradient(#f0f0ee,#c9ab85)"></div><div class="bar"></div></div>
</section>

<section class="welcome">
  <h1>WELCOME TO</h1>
  <h2>VERDANA GLEN CENTER FOR HEALTH &amp; WELLNES</h2>
  <p>Nunc venenatis pharetra lectus, non venenatis dolor rutrum quis. In sed leo mauris. Proin mattis blandit quam, ac congue felis rhoncus quis. Cras sit amet magna ac lorem dignissim ullamcorper. Quisque viverra, quam in venenatis volutpat, mauris libero tempor velit, at consectetur nisi velit quis ante. Mauris porttitor neque sit amet ligula sodales varius. Vestibulum ante ipsum primis in faucibus orci luctus et ultrices posuere cubilia Curae; In vulputate arcu ac felis dictum lobortis. Maecenas sodales, purus nec condimentum facilisis, justo enim blandit arcu, et iaculis lacus tortor semper nisl. Proin ultrices accumsan libero.</p>
  <div class="divider"></div>
  <blockquote class="quote">
    “ Cras ut tortor tincidunt, aliquam nulla et, volutpat ante facilisis convallis<br>massa sagittis molestie fringilla a metu ”
    <cite>- &nbsp;Customer name, City</cite>
  </blockquote>
</section>

<aside class="contact-box">
  <h3>CONTACT US</h3>
  <div class="field">Name</div>
  <div class="field">E-mail</div>
  <div class="field">Phone</div>
  <div class="field message">Messge</div>
  <span class="btn-submit">SUBMIT</span>
</aside>

<section class="info-strip">
  <div class="info" style="left:100px">
    <svg width="20" height="24" viewBox="0 0 20 24"><rect x="1" y="1" width="18" height="22" fill="#888"/><rect x="5" y="4" width="10" height="13" fill="#fff"/></svg>
    <span>55, Building name, streetname<br>City - Zip code</span>
  </div>
  <div class="info" style="left:323px">
    <svg width="24" height="24" viewBox="0 0 26 22"><path d="M3 4c2-3 4-3 5-1l2 3c1 2-1 3-2 4 1 3 3 5 6 6 1-1 2-3 4-2l3 2c2 1 2 3-1 5-6 3-20-10-17-17z" fill="#888"/></svg>
    <span>Phone: 555 301 7712</span>
  </div>
  <div class="info" style="left:534px">
    <svg width="24" height="24" viewBox="0 0 24 24"><rect x="1" y="8" width="22" height="15" fill="#888"/><rect x="6" y="1" width="11" height="8" fill="#aaa"/><rect x="12" y="12" width="8" height="8" fill="#fff"/></svg>
    <span>Fax : 555 301 9064</span>
  </div>
  <div class="info" style="left:741px">
    <svg width="24" height="17" viewBox="0 0 24 17"><rect x="0" y="0" width="24" height="17" fill="#999"/><path d="M0 0l12 9 12-9" stroke="#fff" stroke-width="1.5" fill="none"/></svg>
    <span>E-mail : info@verdanaglen.org</span>
  </div>
</section>

<footer class="site-footer">
  <div class="foot-links">Home<span>|</span>About us<span>|</span>Services<span>|</span>Testimonials<span>|</span>Contact us</div>
  <div class="copyright">Copyright &nbsp;©&nbsp; 2014 &nbsp;Verdana Glen Health and Wellness Center. &nbsp;All rights reserved.</div>
  <div class="social"><i></i><i></i><i></i><i></i></div>
</footer>

</body>
</html>
```